Business Card Design Project

I want a design for my business cards based on an excisting logo design.

Target Market(s)

Marketeers, PR-peeps, CEO's, decisionmakers, entrepreneurs

Industry/Entity Type

Business

Requirements
Nice to have
• Some visual interest on the back too
Should not have
• Sarif on the font

```html
<!DOCTYPE html>
<html lang="nl">
<head>
<meta charset="utf-8">
<title>Leafline PR – visitekaartjes</title>
<link rel="stylesheet" href="https://fonts.googleapis.com/css2?family=Questrial&family=Roboto+Condensed:wght@300;400&family=Arimo:wght@400;700&display=swap">
<style>
  :root {
    --page-bg: #ece8e1;
    --card-top: #fdf3dc;
    --card-bottom: #d6cbb6;
    --ink-grey: #6a6a6a;
    --brand-green: #a5c93a;
    --brand-red: #e4202a;
    --white: #ffffff;
  }
  * { margin: 0; padding: 0; box-sizing: border-box; }
  html, body { width: 1167px; height: 1200px; overflow: hidden; }
  body { background: var(--page-bg); position: relative; }

  .card {
    position: absolute;
    width: 391px;
    height: 705px;
    border-radius: 30px;
    background: linear-gradient(to bottom, var(--card-top) 0%, var(--card-top) 35%, var(--card-bottom) 100%);
    box-shadow: 0 3px 8px rgba(0,0,0,0.25);
    text-align: center;
    overflow: hidden;
    z-index: 2;
  }
  .card--front { left: 197px; top: 141px; }
  .card--back  { left: 635px; top: 146px; }

  .brand-dot {
    position: absolute;
    left: 50%;
    top: 95px;
    width: 170px;
    height: 170px;
    margin-left: -85px;
    border-radius: 50%;
  }
  .brand-dot--red { background: var(--brand-red); }
  .brand-dot--green { background: var(--brand-green); }

  .brand-name {
    position: absolute;
    left: 0; right: 0;
    top: 290px;
    font-family: "Questrial", sans-serif;
    font-size: 44px;
    letter-spacing: 1px;
    color: var(--ink-grey);
  }
  .tagline {
    position: absolute;
    left: 0; right: 0;
    top: 396px;
    font-family: "Roboto Condensed", sans-serif;
    font-size: 22px;
    line-height: 30px;
    color: var(--ink-grey);
  }
  .links {
    position: absolute;
    left: 0; right: 0;
    top: 563px;
    list-style: none;
    font-family: "Roboto Condensed", sans-serif;
    font-size: 22px;
    line-height: 29px;
    color: var(--ink-grey);
  }

  .pull-tab {
    position: absolute;
    left: 238px;
    top: 846px;
    width: 312px;
    height: 244px;
    background: var(--brand-green);
    border-radius: 0 0 26px 26px;
    color: var(--white);
    text-align: center;
    z-index: 1;
  }
  .pull-tab__grip {
    position: absolute;
    left: 328px;
    top: 823px;
    width: 128px;
    height: 32px;
    background: var(--brand-green);
    border-radius: 64px 64px 0 0 / 24px 24px 0 0;
    z-index: 3;
  }
  .contact-name {
    margin-top: 18px;
    font-family: "Questrial", sans-serif;
    font-size: 36px;
    letter-spacing: 0.5px;
  }
  .contact-line {
    font-family: "Arimo", sans-serif;
    font-size: 20px;
    line-height: 26px;
  }
  .contact-email { margin-top: 4px; }
  .contact-phone { margin-top: 14px; font-weight: 700; }
  .contact-address { margin-top: 10px; }
  .chevron { position: absolute; left: 50%; bottom: 8px; margin-left: -14px; }

  .back-grip {
    position: absolute;
    left: 130px;
    top: 683px;
    width: 130px;
    height: 40px;
    background: var(--brand-green);
    border-radius: 65px 65px 0 0 / 24px 24px 0 0;
  }
  .back-grip .chevron { bottom: auto; top: 4px; }
</style>
</head>
<body>

<section class="card card--front">
  <div class="brand-dot brand-dot--red"></div>
  <div class="brand-name">Leafline PR</div>
  <p class="tagline">Systemisch en strategisch PR-,<br>marketing- en communicatieadvies</p>
  <ul class="links">
    <li>leaflinepr.nl</li>
    <li>leaflinepr.nl/news</li>
    <li>leaflinepr.nl/blog</li>
  </ul>
</section>

<div class="pull-tab__grip"></div>
<section class="pull-tab">
  <div class="contact-name">Mara Jansen</div>
  <div class="contact-line contact-email">mara.jansen@leaflinepr.nl</div>
  <div class="contact-line contact-phone">+31(0)6 20481937</div>
  <div class="contact-line contact-address">Lindelaan 42<br>6711 AB Ede</div>
  <svg class="chevron" width="28" height="12" viewBox="0 0 28 12" aria-hidden="true">
    <polyline points="2,2 14,10 26,2" fill="none" stroke="#ffffff" stroke-width="2"/>
  </svg>
</section>

<section class="card card--back">
  <div class="brand-dot brand-dot--green"></div>
  <div class="brand-name">Leafline PR</div>
  <p class="tagline">Systemisch en strategisch PR-,<br>marketing- en communicatieadvies</p>
  <ul class="links">
    <li>leaflinepr.nl</li>
    <li>leaflinepr.nl/news</li>
    <li>leaflinepr.nl/blog</li>
  </ul>
  <div class="back-grip">
    <svg class="chevron" width="28" height="12" viewBox="0 0 28 12" aria-hidden="true">
      <polyline points="2,2 14,10 26,2" fill="none" stroke="#ffffff" stroke-width="2"/>
    </svg>
  </div>
</section>

</body>
</html>
```